Recreate a label for a champagne bottle [See attached example]

I'm needing to recreate a label for a champagne bottle label to give as closing gifts to clients when they purchase a home. Please include the following text "Welcome Home", my initials "R.T", "Established Year", the hashtag #BubTORVA and my logo (attached). I prefer to have a black or white background with a crisp, easy to read cursive font similar to the Dunmore bourbon font. I want it to look as similar of a layout to the Valdorca label as possible

Target Market(s)

Luxury

Font styles to use
Decorative
Script

Colors

Designer to choose only greyscale colors for use in the design.

Requirements
Must have
• "Welcome Home", my initials "R.T", "Established Year", the hashtag #BubTORVA and my logo
Nice to have
• Clean cursive font, easy to read, luxury look.
Should not have
• Clutter, too much design.

```html
<!DOCTYPE html>
<html lang="en">
<head>
<meta charset="utf-8">
<title>Welcome Home – R.T Champagne Label</title>
<link rel="stylesheet" href="https://fonts.googleapis.com/css2?family=Pinyon+Script&family=Montserrat:wght@400;500;600;700&display=swap">
<style>
  :root {
    --backdrop: #000000;
    --gold-dark: #a57f35;
    --gold-light: #e0cf7e;
    --gold-deep: #8d6a2f;
    --label-cream: #f6f5f1;
    --ink: #1b1b1b;
    --muted-gold: #a69b7a;
    --brand-gold: #b8963f;
  }
  html, body {
    margin: 0;
    padding: 0;
    width: 1200px;
    height: 1000px;
    overflow: hidden;
    background: var(--backdrop);
  }
  .canvas {
    position: relative;
    width: 1200px;
    height: 1000px;
    background: var(--backdrop);
  }
  .label-frame {
    position: absolute;
    left: 263px;
    top: 163px;
    width: 672px;
    height: 672px;
    background: linear-gradient(90deg, var(--gold-dark) 0%, var(--gold-light) 47%, var(--gold-deep) 100%);
  }
  .label-panel {
    position: absolute;
    left: 36px;
    top: 36px;
    width: 601px;
    height: 601px;
    background: var(--label-cream);
  }
  .established {
    position: absolute;
    top: 92px;
    left: 0;
    width: 100%;
    display: flex;
    justify-content: center;
    align-items: center;
    gap: 18px;
    font-family: "Montserrat", sans-serif;
    font-size: 11px;
    letter-spacing: 3.5px;
    color: var(--muted-gold);
    line-height: 1;
  }
  .brand-name {
    font-family: "Montserrat", sans-serif;
    font-weight: 600;
    font-size: 18px;
    letter-spacing: 3px;
    color: var(--brand-gold);
  }
  .headline {
    position: absolute;
    left: 0;
    width: 100%;
    box-sizing: border-box;
    text-align: center;
    font-family: "Pinyon Script", cursive;
    color: var(--ink);
    line-height: 1;
    margin: 0;
    font-weight: 400;
    font-size: 132px;
  }
  .headline-welcome {
    top: 178px;
    padding-right: 40px;
  }
  .headline-home {
    top: 318px;
    padding-right: 70px;
  }
  .initials {
    position: absolute;
    top: 448px;
    left: 0;
    width: 100%;
    text-align: center;
    line-height: 1;
  }
  .initials span {
    display: inline-block;
    font-family: "Montserrat", sans-serif;
    font-weight: 700;
    font-size: 42px;
    letter-spacing: 12px;
    padding-left: 12px;
    background: linear-gradient(90deg, var(--gold-dark), var(--gold-light) 55%, var(--gold-deep));
    -webkit-background-clip: text;
    background-clip: text;
    color: transparent;
  }
  .hashtag {
    position: absolute;
    top: 535px;
    left: 0;
    width: 100%;
    text-align: center;
    font-family: "Montserrat", sans-serif;
    font-weight: 500;
    font-size: 22px;
    letter-spacing: 6px;
    color: var(--muted-gold);
    line-height: 1;
  }
  .hashtag strong {
    font-weight: 700;
  }
</style>
</head>
<body>
  <main class="canvas">
    <section class="label-frame">
      <div class="label-panel">
        <div class="established">
          <span>ESTD</span>
          <span class="brand-name">TORVA</span>
          <span>2023</span>
        </div>
        <h1 class="headline headline-welcome">Welcome</h1>
        <h2 class="headline headline-home">Home</h2>
        <div class="initials"><span>R.T</span></div>
        <div class="hashtag">#BUB<strong>TORVA</strong></div>
      </div>
    </section>
  </main>
</body>
</html>
```